Print on top the name of the company: (Or Similar)
Larkmoor Cleaning & Disinfecting
Because your standards aren't standard.

We adhere to ALL NVB guidelines for both residential and commercial cleaning.

Infection Control is our ultimate goal.

Instructions:
Opening a residential and commercial cleaning and disinfecting company in south Florida.

Targeting high-end residential clients, commercial and healthcare facilities, specializing in Ambulatory Care Guidelines. With a concentration and expertise in targeting Covid 19 and other transmissible pathogens.

UMRE trained.
Owned and operated by a licensed BSN Registered Nurse specially ​trained in Infection Control Prevention with over 25 years experience. Over two decades in Ambulatory Surgery Center Administration, Director of Nursing and Infection Control Prevention ad Consulting.

Looking to create a business flier that emphasizes Cleaning & Disinfection
along with the standard expectation for residential and Commercial cleaning services
Updates

Need extra days to review

Target Market(s)

Residential & Commercial

Font styles to use
Decorative

Requirements
Must have
• A checklist for cleaning services

```html
<!DOCTYPE html>
<html lang="en">
<head>
<meta charset="utf-8">
<title>Larkmoor Cleaning &amp; Disinfecting — Flyer</title>
<link rel="stylesheet" href="https://fonts.googleapis.com/css2?family=Bebas+Neue&family=Montserrat:ital,wght@0,300;0,400;0,600;0,700;0,800;1,500&family=Open+Sans:wght@400;600&family=Petit+Formal+Script&display=swap">
<style>
  :root{
    --navy:#0f2a63;
    --navy-deep:#0b2156;
    --sky:#2a93d5;
    --grey-band:#d3d5da;
    --grey-rule:#8a8d93;
    --white:#ffffff;
    --ink:#1b2236;
    --photo-light:#e7e8ea;
    --photo-mid:#b9bcc1;
  }
  *{margin:0;padding:0;box-sizing:border-box}
  html,body{width:900px;height:1200px;overflow:hidden;background:var(--white)}
  .flyer{position:relative;width:900px;height:1200px;background:var(--white);overflow:hidden;font-family:"Montserrat",sans-serif;color:var(--navy)}

  .hero-panel{position:absolute;left:0;top:17px;width:900px;height:456px;background:var(--navy)}
  .hero-art{position:absolute;left:0;top:0;width:900px;height:480px}

  .brand-mark{position:absolute;left:66px;top:56px;display:flex;align-items:center;gap:14px}
  .brand-mark__circle{width:120px;height:120px;border-radius:50%;background:var(--white)}
  .brand-mark__name{font-weight:700;font-size:20px;color:var(--white);letter-spacing:1px}

  .title{position:absolute;left:64px;top:222px;color:var(--white)}
  .title__main{font-family:"Bebas Neue",sans-serif;font-size:76px;line-height:70px;letter-spacing:1px;font-weight:400}
  .title__sub{font-family:"Montserrat",sans-serif;font-weight:300;font-size:34px;margin-top:4px}
  .title__tagline{font-family:"Montserrat",sans-serif;font-style:italic;font-weight:500;font-size:17px;margin-top:12px;color:var(--white)}

  .pledge{position:absolute;left:66px;top:500px;width:780px;font-weight:800;font-size:26px;line-height:36px;letter-spacing:.6px;color:var(--navy);text-transform:uppercase}
  .pledge-rule{position:absolute;left:66px;top:588px;width:376px;height:4px;background:var(--grey-rule)}
  .goal{position:absolute;left:66px;top:602px;font-weight:700;font-size:27px;color:var(--sky)}
  .intro{position:absolute;left:66px;top:640px;width:780px;font-family:"Petit Formal Script",cursive;font-size:21px;line-height:34px;color:var(--ink)}
  .intro strong{font-weight:400;font-size:23px}

  .checklist{position:absolute;left:66px;top:716px;width:780px}
  .checklist__head{font-weight:700;font-size:16px;color:var(--navy);text-transform:uppercase;letter-spacing:.6px;margin-bottom:6px}
  .checklist__items{list-style:none;display:grid;grid-template-columns:repeat(3,1fr);row-gap:6px;column-gap:10px}
  .checklist__item{display:flex;align-items:center;gap:8px;font-weight:600;font-size:14px;color:var(--ink);white-space:nowrap}
  .checklist__tick{width:18px;height:18px;flex:none}

  .targets{position:absolute;left:0;top:814px;width:900px;height:170px;background:var(--grey-band)}
  .targets__tab{position:absolute;left:300px;top:-14px;width:317px;height:52px}
  .targets__label{position:absolute;left:300px;top:-14px;width:317px;height:52px;display:flex;align-items:center;justify-content:center;padding-top:8px;font-weight:800;font-size:30px;letter-spacing:1px;color:var(--white)}
  .targets__divider{position:absolute;left:432px;top:52px;height:106px;border-left:2px dashed var(--grey-rule)}
  .target{position:absolute;display:flex;align-items:center;gap:14px;font-weight:600;font-size:16px;line-height:20px;color:var(--ink)}
  .target__icon{width:50px;height:50px;flex:none}
  .target--a{left:66px;top:46px}
  .target--b{left:66px;top:108px}
  .target--c{left:500px;top:46px}
  .target--d{left:500px;top:108px}

  .credentials{position:absolute;left:66px;top:1000px;width:780px;color:var(--navy)}
  .credentials__head{font-weight:700;font-size:18px;margin-bottom:6px}
  .credentials__body{font-family:"Open Sans",sans-serif;font-size:13.6px;line-height:17px;color:var(--ink)}

  .footer{position:absolute;left:0;top:1117px;width:900px;height:78px;background:var(--navy);display:flex;align-items:center;justify-content:center}
  .footer__url{font-weight:700;font-size:21px;color:var(--white);letter-spacing:.3px}
</style>
</head>
<body>
<main class="flyer">
  <div class="hero-panel"></div>

  <svg class="hero-art" viewBox="0 0 900 480">
    <defs>
      <clipPath id="photoClip"><circle cx="850" cy="-30" r="490"/></clipPath>
      <linearGradient id="photoTone" x1="0" y1="0" x2="1" y2="1">
        <stop offset="0" stop-color="#b9bcc1"/>
        <stop offset=".55" stop-color="#e7e8ea"/>
        <stop offset="1" stop-color="#c9cbcf"/>
      </linearGradient>
    </defs>
    <circle cx="850" cy="-30" r="504" fill="none" stroke="#2a93d5" stroke-width="5"/>
    <circle cx="850" cy="-30" r="496" fill="#ffffff"/>
    <g clip-path="url(#photoClip)" role="img" aria-label="Photo of a purple-gloved hand wiping a grey counter with a pink cloth beside a spray bottle">
      <rect x="300" y="0" width="600" height="480" fill="url(#photoTone)"/>
    </g>
  </svg>

  <div class="brand-mark">
    <div class="brand-mark__circle"></div>
    <span class="brand-mark__name">Larkmoor</span>
  </div>

  <h1 class="title">
    <div class="title__main">LARKMOOR<br>CLEANING</div>
    <div class="title__sub">&amp; Disinfecting</div>
    <div class="title__tagline">Because your standards aren't standard.</div>
  </h1>

  <p class="pledge">We adhere to all NVB guidelines for both residential and commercial cleaning.</p>
  <div class="pledge-rule"></div>
  <p class="goal">Infection Control is our ultimate goal.</p>
  <p class="intro">Opening a residential and commercial cleaning and disinfecting company in <strong>South Florida</strong>.</p>

  <section class="checklist">
    <h2 class="checklist__head">Our cleaning checklist</h2>
    <ul class="checklist__items">
      <li class="checklist__item"><svg class="checklist__tick" viewBox="0 0 18 18" aria-hidden="true"><circle cx="9" cy="9" r="9" fill="var(--sky)"/><path d="M5 9.5 L8 12.5 L13 6" fill="none" stroke="var(--white)" stroke-width="2"/></svg>Surface disinfection</li>
      <li class="checklist__item"><svg class="checklist__tick" viewBox="0 0 18 18" aria-hidden="true"><circle cx="9" cy="9" r="9" fill="var(--sky)"/><path d="M5 9.5 L8 12.5 L13 6" fill="none" stroke="var(--white)" stroke-width="2"/></svg>High-touch point wiping</li>
      <li class="checklist__item"><svg class="checklist__tick" viewBox="0 0 18 18" aria-hidden="true"><circle cx="9" cy="9" r="9" fill="var(--sky)"/><path d="M5 9.5 L8 12.5 L13 6" fill="none" stroke="var(--white)" stroke-width="2"/></svg>Kitchens &amp; bathrooms</li>
      <li class="checklist__item"><svg class="checklist__tick" viewBox="0 0 18 18" aria-hidden="true"><circle cx="9" cy="9" r="9" fill="var(--sky)"/><path d="M5 9.5 L8 12.5 L13 6" fill="none" stroke="var(--white)" stroke-width="2"/></svg>Floors vacuumed &amp; mopped</li>
      <li class="checklist__item"><svg class="checklist__tick" viewBox="0 0 18 18" aria-hidden="true"><circle cx="9" cy="9" r="9" fill="var(--sky)"/><path d="M5 9.5 L8 12.5 L13 6" fill="none" stroke="var(--white)" stroke-width="2"/></svg>Dusting &amp; trash removal</li>
      <li class="checklist__item"><svg class="checklist__tick" viewBox="0 0 18 18" aria-hidden="true"><circle cx="9" cy="9" r="9" fill="var(--sky)"/><path d="M5 9.5 L8 12.5 L13 6" fill="none" stroke="var(--white)" stroke-width="2"/></svg>Medical-grade sanitizing</li>
    </ul>
  </section>

  <section class="targets">
    <svg class="targets__tab" viewBox="0 0 317 52" aria-hidden="true">
      <polygon points="0,14 12,0 12,14" fill="var(--navy-deep)"/>
      <polygon points="317,14 305,0 305,14" fill="var(--navy-deep)"/>
      <rect x="12" y="0" width="293" height="4" fill="var(--navy-deep)"/>
      <rect x="0" y="10" width="317" height="42" fill="var(--navy)"/>
    </svg>
    <div class="targets__label">TARGETING</div>
    <div class="targets__divider"></div>

    <div class="target target--a">
      <svg class="target__icon" viewBox="0 0 50 50" aria-hidden="true">
        <circle cx="25" cy="25" r="23" fill="none" stroke="var(--sky)" stroke-width="3"/>
        <circle cx="25" cy="25" r="19" fill="var(--navy)"/>
        <path d="M15 25 L25 16 L35 25 M18 23 V34 H32 V23" fill="none" stroke="var(--white)" stroke-width="2"/>
      </svg>
      <span>High-end residential clients</span>
    </div>
    <div class="target target--b">
      <svg class="target__icon" viewBox="0 0 50 50" aria-hidden="true">
        <circle cx="25" cy="25" r="23" fill="none" stroke="var(--sky)" stroke-width="3"/>
        <circle cx="25" cy="25" r="19" fill="var(--navy)"/>
        <path d="M17 35 V17 H29 V35 M29 23 H34 V35 M15 35 H36 M20 21 H26 M20 26 H26" fill="none" stroke="var(--white)" stroke-width="2"/>
      </svg>
      <span>Commercial</span>
    </div>
    <div class="target target--c">
      <svg class="target__icon" viewBox="0 0 50 50" aria-hidden="true">
        <circle cx="25" cy="25" r="23" fill="none" stroke="var(--sky)" stroke-width="3"/>
        <circle cx="25" cy="25" r="19" fill="var(--navy)"/>
        <rect x="16" y="16" width="18" height="18" fill="none" stroke="var(--white)" stroke-width="2"/>
        <path d="M25 19 V31 M19 25 H31" stroke="var(--white)" stroke-width="2.5"/>
      </svg>
      <span>Healthcare facilities</span>
    </div>
    <div class="target target--d">
      <svg class="target__icon" viewBox="0 0 50 50" aria-hidden="true">
        <circle cx="25" cy="25" r="23" fill="none" stroke="var(--sky)" stroke-width="3"/>
        <circle cx="25" cy="25" r="19" fill="var(--navy)"/>
        <rect x="17" y="15" width="16" height="20" fill="none" stroke="var(--white)" stroke-width="2"/>
        <path d="M20 22 L22 24 L25 20 M20 29 L22 31 L25 27 M27 23 H31 M27 30 H31" fill="none" stroke="var(--white)" stroke-width="1.6"/>
      </svg>
      <span>Specializing in Ambulatory Care<br>Guidelines.</span>
    </div>
  </section>

  <section class="credentials">
    <p class="credentials__head">UMRE trained.</p>
    <p class="credentials__body">Owned and operated by a licensed BSN Registered Nurse specially trained in Infection Control Prevention with over 25 years experience. Over two decades in Ambulatory Surgery Center Administration, Director of Nursing and Infection Control Prevention ad Consulting.</p>
  </section>

  <footer class="footer">
    <span class="footer__url">www.larkmoorclean.com</span>
  </footer>
</main>
</body>
</html>
```